Security doors and flyscreens

We need business cards for our company called K & R Traders. We quote, manufacture and install security doors and flyscreens.

Industry/Entity Type

Security

Contact Information for Business Card

K & R TRADERS
17 Larkfield Ave. Thomastown 3074
Ph: 8127 5506
Fax: 8127 5502
Colin: 0417 952 160
Email: gatemakerhub@mailbox-example.net

```html
<!DOCTYPE html>
<html lang="en">
<head>
<meta charset="utf-8">
<title>K &amp; R Traders – Business Card</title>
<link rel="stylesheet" href="https://fonts.googleapis.com/css2?family=Open+Sans:wght@400;600;700;800&display=swap">
<style>
  :root {
    --page-bg: #e9eaec;
    --card-white: #ffffff;
    --card-grey: #e4e5e7;
    --ink: #3a3d42;
    --ink-soft: #5a5e64;
    --brand-blue: #2f6fd6;
    --band-deep: #1f4fc4;
    --band-light: #1ea0ec;
    --swoosh-grey: #8b8f95;
    --divider: #9aa0a6;
  }
  * { margin: 0; padding: 0; box-sizing: border-box; }
  html, body {
    width: 1200px; height: 899px; overflow: hidden;
    background: var(--page-bg);
    font-family: "Open Sans", sans-serif;
    color: var(--ink);
  }
  .card {
    position: absolute; left: 150px; top: 192px;
    width: 900px; height: 514px;
    border-radius: 44px; overflow: hidden;
    background: linear-gradient(180deg, var(--card-white) 0%, var(--card-white) 40%, var(--card-grey) 75%);
    box-shadow: 0 14px 40px rgba(0,0,0,.18);
  }
  .card-band { position: absolute; left: 0; top: 0; width: 900px; height: 514px; }
  .brand {
    position: absolute; left: 150px; top: 52px;
    display: flex; align-items: center; gap: 18px;
  }
  .brand-mark {
    width: 66px; height: 66px; border-radius: 50%;
    background: var(--brand-blue);
  }
  .brand-name {
    font-weight: 800; font-size: 34px; letter-spacing: .5px;
    color: var(--brand-blue);
  }
  .person {
    position: absolute; right: 470px; top: 160px;
    text-align: right;
  }
  .person-name { font-weight: 700; font-size: 22px; line-height: 1.2; }
  .person-role { font-size: 17px; color: var(--ink-soft); margin-bottom: 22px; }
  .person-address { font-size: 17px; color: var(--ink-soft); line-height: 1.4; width: 230px; margin-left: auto; }
  .divider {
    position: absolute; left: 452px; top: 160px;
    width: 1.5px; height: 146px; background: var(--divider);
  }
  .contacts {
    position: absolute; left: 468px; top: 160px;
    list-style: none;
  }
  .contacts li {
    display: flex; align-items: center; gap: 10px;
    font-size: 16px; line-height: 28px; color: var(--ink-soft);
  }
  .contact-icon {
    width: 18px; height: 18px; border-radius: 50%;
    background: var(--ink); flex: none;
    display: flex; align-items: center; justify-content: center;
  }
  .contact-icon svg { width: 11px; height: 11px; }
</style>
</head>
<body>
  <div class="card">
    <svg class="card-band" viewBox="0 0 900 514" aria-hidden="true">
      <defs>
        <linearGradient id="band-fill" x1="0" y1="0" x2="1" y2="0">
          <stop offset="0" stop-color="#1f4fc4"/>
          <stop offset=".55" stop-color="#1ea0ec"/>
          <stop offset="1" stop-color="#1f4fc4"/>
        </linearGradient>
        <linearGradient id="swoosh-fill" x1="0" y1="0" x2="1" y2="0">
          <stop offset="0" stop-color="#c9ccd0"/>
          <stop offset=".4" stop-color="#8b8f95"/>
          <stop offset="1" stop-color="#5d6167"/>
        </linearGradient>
      </defs>
      <path d="M0 322 C 250 338, 560 366, 900 432 L 900 416 C 560 350, 250 322, 0 308 Z" fill="url(#swoosh-fill)"/>
      <path d="M0 340 C 250 356, 560 386, 900 448 L 900 514 L 0 514 Z" fill="url(#band-fill)"/>
    </svg>

    <div class="brand">
      <span class="brand-mark"></span>
      <span class="brand-name">K &amp; R TRADERS</span>
    </div>

    <div class="person">
      <p class="person-name">Colin</p>
      <p class="person-role">Owner / C.E.O</p>
      <p class="person-address">17 Larkfield Ave. Thomastown 3074</p>
    </div>

    <div class="divider"></div>

    <ul class="contacts">
      <li><span class="contact-icon"><svg viewBox="0 0 12 12"><path d="M3 1l2 2-1 1.5a6 6 0 0 0 3.5 3.5L9 7l2 2-1.5 2A9 9 0 0 1 1 2.5Z" fill="#fff"/></svg></span>8127 5506</li>
      <li><span class="contact-icon"><svg viewBox="0 0 12 12"><rect x="2" y="4" width="8" height="5" fill="#fff"/><rect x="3.5" y="1.5" width="5" height="3" fill="#fff"/></svg></span>8127 5502</li>
      <li><span class="contact-icon"><svg viewBox="0 0 12 12"><rect x="3.5" y="1" width="5" height="10" rx="1" fill="#fff"/></svg></span>0417 952 160</li>
      <li><span class="contact-icon"><svg viewBox="0 0 12 12"><rect x="1.5" y="3" width="9" height="6" fill="#fff"/><path d="M1.5 3l4.5 3.5L10.5 3" stroke="#3a3d42" fill="none"/></svg></span>gatemakerhub@mailbox-example.net</li>
      <li><span class="contact-icon"><svg viewBox="0 0 12 12"><circle cx="6" cy="6" r="4.2" stroke="#fff" fill="none"/><path d="M1.8 6h8.4M6 1.8v8.4" stroke="#fff"/></svg></span>www.krtraders-example.net</li>
    </ul>
  </div>
</body>
</html>
```